Box Design of "pet rapid test for dogs & cats" with professional use

"The market is in Southeast Asia, South America, Europe, and the U.S."
Clients: Veterinary clinics, pet hospitals,(a small number of home use)

Primary colors:
Orange, Green,or Blue, (select 1,or 2 color)
Neutrals: Black, Gray, or White (optional)
Dimensions:135mm(L)*90mm(W)*105mm(W)

Kindly review the attached file for additional content
Updates

I have increased my budget, please provide a satisfactory design solution, thank you very much for your work.

Target Market(s)

Southeast Asia, South America, Europe, and the U.S.

Industry/Entity Type

Veterinary test kit for dogs & cats

Colors
0054AA
0677BA
7BADD7
CADEEF
E8F1F8
0094D4
00A9DD
6FCCEA
C7EBF8
E9F6FB
00AB8E
00BBA5
67D7C9
C6EFE9
E9F9F6
59FF00
82FF00
B8FF75
E3FFCB
F4FFEA
F0912C
F2A743
F7CA91
FBE8D2
FDF5EE
EE7325
F08F49
F5BC92
FAE3D3
FDF4ED

Requirements
Nice to have
• Appealing Box Appearance with professional

```html
<!DOCTYPE html>
<html lang="en">
<head>
<meta charset="utf-8">
<title>PawScan Pet Rapid Test Kit – Box Dieline</title>
<link href="https://fonts.googleapis.com/css2?family=Montserrat:wght@600;700;800&family=Open+Sans:wght@400;600;700&display=swap" rel="stylesheet">
<style>
  :root{
    --green:#13711a;
    --orange:#f28a10;
    --orange-deep:#ee7325;
    --ink:#111;
    --line:#8a8a8a;
    --white:#fff;
  }
  *{box-sizing:border-box;margin:0;padding:0}
  html,body{width:1200px;height:1200px;overflow:hidden;background:var(--white)}
  body{position:relative;font-family:"Open Sans",Arial,sans-serif;color:var(--ink)}
  .dieline{position:absolute;left:0;top:0}
  .dims{position:absolute;left:314px;top:80px;font-size:16px;font-family:"Open Sans",Arial,sans-serif}
  .panel{position:absolute;top:272px;height:237px;overflow:hidden}
  .panel--green{background:var(--green);color:var(--white)}
  .p1{left:67px;width:205px;padding:14px 11px}
  .p2{left:272px;width:306px;padding:16px 23px}
  .p3{left:578px;width:204px;padding:14px 11px}
  .p4{left:782px;width:306px;padding:16px 23px}
  .brand{font-family:"Montserrat",Arial,sans-serif;font-weight:800;font-size:17px;display:flex;align-items:center;gap:5px;letter-spacing:-.2px}
  .brand::before{content:"";width:13px;height:13px;border-radius:50%;background:var(--orange)}
  .brand--white{color:var(--white)}
  .brand--green{color:var(--green)}
  .tagline{font-family:"Montserrat",Arial,sans-serif;font-weight:700;color:var(--orange);font-size:11px;margin-top:2px}
  .feature{margin-top:10px;font-size:7.4px;line-height:1.22}
  .feature h4{font-family:"Montserrat",Arial,sans-serif;font-weight:700;font-size:7.4px;margin-bottom:1px}
  .title-bar{background:var(--green);color:var(--white);font-family:"Montserrat",Arial,sans-serif;font-weight:600;font-size:10.5px;line-height:1.3;padding:3px 5px;margin-top:6px;width:258px}
  .contents{margin-top:5px;font-size:8.8px;line-height:1.3;width:150px}
  .contents strong{font-weight:700}
  .mark{position:absolute;right:48px;top:96px;width:60px;height:56px;border-radius:6px;background:linear-gradient(150deg,#e8f0e8,#c9dfca)}
  .storage{position:absolute;left:23px;top:170px;font-size:9px;line-height:1.3}
  .count{position:absolute;right:23px;top:168px;background:var(--green);color:var(--white);font-family:"Montserrat",Arial,sans-serif;font-weight:700;font-size:8.5px;padding:1px 3px}
  .symbols{position:absolute;left:31px;top:196px}
  .p3 .brand{justify-content:center}
  .subtitle{text-align:center;font-family:"Montserrat",Arial,sans-serif;font-weight:700;font-size:10.5px;margin-top:2px}
  .p3 .feature{margin-top:8px;font-size:7.2px}
  .maker{text-align:center;font-family:"Montserrat",Arial,sans-serif;font-weight:700;color:var(--orange);font-size:10.5px;margin-top:5px;line-height:1.45}
  .lid{position:absolute;left:782px;top:67px;width:306px;height:205px;transform:rotate(180deg)}
  .lid__band{background:var(--green);color:var(--white);font-family:"Montserrat",Arial,sans-serif;font-weight:700;height:20px;display:flex;align-items:center;justify-content:center}
  .lid__band--top{font-size:11px;letter-spacing:.3px}
  .lid__band--tag{height:37px;font-size:14.5px;letter-spacing:.4px}
  .lid__photo{height:148px;position:relative;background:linear-gradient(90deg,#f08a0a 0%,#f59a2c 45%,#ee7a14 100%)}
  .lid__photo .brand{position:absolute;right:20px;top:10px;color:var(--white);font-size:16px;flex-direction:row-reverse}
  .lid__photo .brand::before{background:var(--white)}
</style>
</head>
<body>
  <div class="dims">135mm*90mm*105mm</div>

  <svg class="dieline" width="1200" height="1200" viewBox="0 0 1200 1200" fill="none" stroke="#8a8a8a" stroke-width="1">
    <path d="M67 272 L73 266 L73 181 L253 181 Q262 181 262 190 L262 266 L272 272"/>
    <path d="M578 272 L589 266 L589 198 Q589 181 605 181 L776 181 L776 272"/>
    <path d="M782 272 L782 46 Q782 22 806 22 L1064 22 Q1088 22 1088 46 L1088 272"/>
    <path d="M1088 272 L1134 278 L1134 502 L1088 509"/>
    <path d="M67 509 L170 578 L170 621 L272 621 L272 509"/>
    <path d="M272 509 L340 608 L340 640 Q340 656 356 656 L494 656 Q510 656 510 640 L510 608 L578 509"/>
    <path d="M578 509 L578 621 L680 621 L680 578 L782 509"/>
    <path d="M782 509 L782 658 L832 658 Q850 658 850 640 L850 612 L1020 612 L1020 640 Q1020 658 1038 658 L1088 658 L1088 509"/>
  </svg>

  <div class="lid">
    <div class="lid__band lid__band--top">PET RAPID TEST KIT for Dogs &amp; Cats</div>
    <div class="lid__photo" role="img" aria-label="Photo of a dog and a cat in warm orange tones">
      <div class="brand">PawScan</div>
    </div>
    <div class="lid__band lid__band--tag">Loved by Pets, Trusted by Vets</div>
  </div>

  <section class="panel panel--green p1">
    <div class="brand brand--white">PawScan</div>
    <div class="tagline">Loved by Pets, Trusted by Vets</div>
    <div class="feature"><h4>FÁCIL Y PRÁCTICO:</h4>• Sin capacitación previa<br>• Suficientemente simple para uso en casa</div>
    <div class="feature"><h4>RÁPIDO Y EFICIENTE:</h4>• Resultados digitales en &lt;10 minutos<br>• Desde inicio hasta resultado final</div>
    <div class="feature"><h4>PRECISO Y FIABLE:</h4>• Resultados rápidos y confiables con tecnología de inmunocromatografía avanzada<br>• Validado por clínicas veterinarias a nivel global</div>
    <div class="feature"><h4>DETECCIÓN MULTIENFERMEDADES:</h4>• Evalúa múltiples patologías simultáneamente<br>• Ayudar a los dueños de mascotas a detectar problemas a tiempo</div>
  </section>

  <section class="panel p2">
    <div class="brand brand--green">PawScan</div>
    <div class="title-bar">PET RAPID TEST KIT for Dogs &amp; Cats<br>Loved by Pets, Trusted by Vets</div>
    <div class="contents"><strong>Contents</strong><br>(1) Test Kits(Cassette,disposable dropper,desiccant).<br>(2) Assay buffer.<br>(3) Sterile swabs.<br>(4) Instruction manual.</div>
    <div class="mark" role="img" aria-label="Line drawing of a dog and cat with a green tick"></div>
    <div class="storage">Store at 2-30˚<br>Avoid direct sunlight</div>
    <div class="count">10 Tests/Box</div>
    <svg class="symbols" width="240" height="34" viewBox="0 0 240 34" stroke="#111" fill="none" stroke-width="1.2">
      <rect x="0" y="8" width="36" height="20"/><text x="4" y="24" font-family="Montserrat,Arial,sans-serif" font-weight="700" font-size="14" fill="#111" stroke="none">IVD</text>
      <text x="46" y="25" font-size="7" fill="#111" stroke="none" font-family="Open Sans,Arial,sans-serif">2°C</text>
      <line x1="66" y1="2" x2="66" y2="26"/><circle cx="66" cy="29" r="3" fill="#111"/><line x1="66" y1="6" x2="72" y2="6"/>
      <text x="74" y="9" font-size="7" fill="#111" stroke="none" font-family="Open Sans,Arial,sans-serif">30°C</text>
      <circle cx="113" cy="9" r="3" fill="#111"/>
      <path d="M113 1v3M113 14v3M105 9h3M118 9h3M107 3l2 2M117 13l2 2M119 3l-2 2M107 15l2-2"/>
      <path d="M96 22 L110 14"/><rect x="98" y="24" width="6" height="6" fill="#111"/>
      <path d="M163 10 L177 8 L177 30 L163 31 Z M177 8 L190 10 L190 31 L177 30"/>
      <text x="181" y="29" font-family="Open Sans,Arial,sans-serif" font-weight="700" font-size="15" fill="#111" stroke="none">i</text>
      <circle cx="220" cy="18" r="12"/><text x="214" y="25" font-size="18" fill="#111" stroke="none" font-family="Open Sans,Arial,sans-serif">2</text><line x1="211" y1="10" x2="229" y2="26"/>
    </svg>
  </section>

  <section class="panel panel--green p3">
    <div class="brand brand--white">PawScan</div>
    <div class="subtitle">Rapid Test kit</div>
    <div class="feature"><h4>SIMPLE &amp; CONVENIENT:</h4>No professional skills required,Simple enough for home use.</div>
    <div class="feature"><h4>FAST &amp; EFFICIENT:</h4>Digital results in &lt; 10 minutes - from start to completion.</div>
    <div class="feature"><h4>ACCURATE &amp; RELIABLE</h4>Quick and trustworthy pet health results using advanced lateral flowbiotech,Trusted by vet clinics worldwide.</div>
    <div class="feature"><h4 style="display:inline">SUPPORTS SCREENING OF MULTIPLE DISEASES</h4> Helping pet owners detect issues early.</div>
    <div class="maker">MADE by VETMARA™<br>Loved by Pets, Trusted by Vets</div>
  </section>

  <section class="panel p4">
    <div class="brand brand--green">PawScan</div>
    <div class="title-bar">PET RAPID TEST KIT for Dogs &amp; Cats<br>Loved by Pets, Trusted by Vets</div>
    <div class="contents"><strong>Contents</strong><br>(1) Test Kits(Cassette,disposable dropper,desiccant).<br>(2) Assay buffer.<br>(3) Sterile swabs.<br>(4) Instruction manual.</div>
    <div class="mark" role="img" aria-label="Line drawing of a dog and cat with a green tick"></div>
    <div class="storage">Store at 2-30˚<br>Avoid direct sunlight</div>
    <div class="count">10 Tests/Box</div>
    <svg class="symbols" width="240" height="34" viewBox="0 0 240 34" stroke="#111" fill="none" stroke-width="1.2">
      <rect x="0" y="8" width="36" height="20"/><text x="4" y="24" font-family="Montserrat,Arial,sans-serif" font-weight="700" font-size="14" fill="#111" stroke="none">IVD</text>
      <text x="46" y="25" font-size="7" fill="#111" stroke="none" font-family="Open Sans,Arial,sans-serif">2°C</text>
      <line x1="66" y1="2" x2="66" y2="26"/><circle cx="66" cy="29" r="3" fill="#111"/><line x1="66" y1="6" x2="72" y2="6"/>
      <text x="74" y="9" font-size="7" fill="#111" stroke="none" font-family="Open Sans,Arial,sans-serif">30°C</text>
      <circle cx="113" cy="9" r="3" fill="#111"/>
      <path d="M113 1v3M113 14v3M105 9h3M118 9h3M107 3l2 2M117 13l2 2M119 3l-2 2M107 15l2-2"/>
      <path d="M96 22 L110 14"/><rect x="98" y="24" width="6" height="6" fill="#111"/>
      <path d="M163 10 L177 8 L177 30 L163 31 Z M177 8 L190 10 L190 31 L177 30"/>
      <text x="181" y="29" font-family="Open Sans,Arial,sans-serif" font-weight="700" font-size="15" fill="#111" stroke="none">i</text>
      <circle cx="220" cy="18" r="12"/><text x="214" y="25" font-size="18" fill="#111" stroke="none" font-family="Open Sans,Arial,sans-serif">2</text><line x1="211" y1="10" x2="229" y2="26"/>
    </svg>
  </section>
</body>
</html>
```